We need a business card design, letterhead design and envelope design for our corporate image

We are looking for a corporate business card design, letterhead and envelope design to match the business card design. Logo is done.

```html
<!DOCTYPE html>
<html lang="en">
<head>
<meta charset="utf-8">
<title>Norvane Business Card</title>
<link href="https://fonts.googleapis.com/css2?family=Roboto:wght@400;500;700&display=swap" rel="stylesheet">
<style>
  :root {
    --bg: #1c1c1e;
    --card: #f4f4f4;
    --accent: #f2d21a;
    --ink: #5a5a5a;
    --rule: #6e6e6e;
  }
  html, body {
    margin: 0;
    padding: 0;
    width: 1200px;
    height: 900px;
    overflow: hidden;
    background: var(--bg);
    font-family: "Roboto", Arial, sans-serif;
  }
  .canvas {
    width: 1200px;
    height: 900px;
    display: flex;
    align-items: center;
    justify-content: center;
  }
  .card {
    position: relative;
    width: 1050px;
    height: 600px;
    background: var(--card);
    border-bottom: 6px solid var(--accent);
    box-sizing: border-box;
  }
  .holder {
    position: absolute;
    left: 80px;
    top: 120px;
  }
  .holder-name {
    margin: 0;
    color: var(--accent);
    font-weight: 700;
    font-size: 34px;
    letter-spacing: 0.5px;
    text-transform: uppercase;
  }
  .holder-role {
    margin: 4px 0 0;
    color: var(--ink);
    font-weight: 500;
    font-size: 30px;
  }
  .divider {
    position: absolute;
    left: 400px;
    top: 208px;
    width: 570px;
    height: 2px;
    background: var(--rule);
  }
  .contacts {
    position: absolute;
    left: 80px;
    top: 240px;
    list-style: none;
    margin: 0;
    padding: 0;
  }
  .contact-item {
    display: flex;
    align-items: center;
    gap: 16px;
    color: var(--ink);
    font-size: 28px;
    line-height: 44px;
  }
  .contact-icon {
    width: 26px;
    height: 26px;
    flex: none;
  }
  .brand-name {
    position: absolute;
    right: 100px;
    top: 82px;
    margin: 0;
    color: var(--ink);
    font-weight: 700;
    font-size: 68px;
    line-height: 1;
  }
  .address {
    position: absolute;
    right: 80px;
    bottom: 70px;
    text-align: right;
    font-style: normal;
    color: var(--ink);
    font-size: 32px;
    line-height: 42px;
  }
  .address-company {
    color: var(--accent);
    font-weight: 500;
  }
</style>
</head>
<body>
<main class="canvas">
  <section class="card">
    <div class="holder">
      <h1 class="holder-name">Martin Alderbrook</h1>
      <p class="holder-role">Managing Director</p>
    </div>

    <p class="brand-name">Norvane</p>

    <div class="divider"></div>

    <ul class="contacts">
      <li class="contact-item">
        <svg class="contact-icon" viewBox="0 0 24 24" aria-hidden="true">
          <path fill="#f2d21a" d="M6.6 10.8a15.2 15.2 0 0 0 6.6 6.6l2.2-2.2c.3-.3.7-.4 1-.2 1.1.4 2.3.6 3.6.6.6 0 1 .4 1 1V20c0 .6-.4 1-1 1A17 17 0 0 1 3 4c0-.6.4-1 1-1h3.5c.6 0 1 .4 1 1 0 1.3.2 2.5.6 3.6.1.3 0 .7-.2 1z"/>
        </svg>
        <span>+15550142376</span>
      </li>
      <li class="contact-item">
        <svg class="contact-icon" viewBox="0 0 24 24" aria-hidden="true">
          <rect x="2" y="5" width="20" height="14" rx="1" fill="#f2d21a"/>
          <path d="M2.5 5.5 12 13l9.5-7.5" fill="none" stroke="#f4f4f4" stroke-width="1.6"/>
        </svg>
        <span>martin@norvane-studio.com</span>
      </li>
      <li class="contact-item">
        <svg class="contact-icon" viewBox="0 0 24 24" aria-hidden="true">
          <g fill="none" stroke="#f2d21a" stroke-width="2">
            <circle cx="12" cy="12" r="9"/>
            <ellipse cx="12" cy="12" rx="4" ry="9"/>
            <path d="M3 12h18"/>
          </g>
        </svg>
        <span>www.norvane-studio.com</span>
      </li>
    </ul>

    <address class="address">
      <span class="address-company">Norvane Ltd</span><br>
      48 Cedar Ridge Lane<br>
      Maple Falls, ON K2B 7T4
    </address>
  </section>
</main>
</body>
</html>
```